Fern Lodge Painting, Eco and Non toxic painting client information brochure.

Fern lodge painting is a painting company that specialises in eco and non toxic paints. This brochure will be left with the client after the initial meeting to explain about my business and hopefully win the job. By reading the text i have provided (see attachment) you can get a better understanding of what we do.
The brochure should be fresh and clean looking, complimenting the Fern Lodge Painting logo and the text provided.
This will be printed onto a recycled paper.
Text and font must clear and easy to read.

Please have a look at my web page. I will be redoing this soon as well but this will give you some ideas of where I'm at.

Would like some picture but not sure what.
I have attached some pics but they don't have to be use
Updates

Hi peeps,

Thanks for all the great designs and sorry i haven't got back to you sooner.
been a bit busy.
Tomorrow i hope to be able to sit down and have a good look at what everybody has done.
Thanks again i really appreciate the effort.

kind regards gordon 

hi designers,

Just sat down and had a good look at the designs sent in and there are some crackers.
Its going to be very difficult to choose. I have only 1 day left before it closes so ill wait till then to see if there are any more submissions come in then ill get back to everybody.
Thanks again for your time and effort.

kind regards gordon 

Hi too all you designers that have worked on my project. 

I am always amazed at all the different designs that come through. Super work guys and girls. 
I have narrowed it down to a couple of designs.
Ill be making the decision tonight.
Thanks again to you all and i really appreciate all the hard work.
I will be doing another brochure in the future for more architecture / builder focus and there were a few designs that would work perfectly for this.

Kinds regards gordon  

Target Market(s)

The work we do is mainly residential repaints, family homes
Mostly I am dealing with the wife of the family or female designers/architects

Industry/Entity Type

Painting

Requirements
Must have
• Company logo, either white or black version what ever suits best.
Text that has been provided.
Brochure will be 1 page A 4, folded into 3 parts both sides.
Front page must have logo and
SPECIALSING IN:
NON TOXIC
ECO FRIENDLY &
HEAT REFLECTIVE PAINTS
Phone 040 318 2694
Painting@fernlodge.biz
www.fernlodge.biz

```html
<!DOCTYPE html>
<html lang="en">
<head>
<meta charset="utf-8">
<title>Fern Lodge Painting – Brochure</title>
<link rel="stylesheet" href="https://fonts.googleapis.com/css2?family=Dosis:wght@600;700&family=PT+Sans:wght@400;700&family=Quicksand:wght@300&display=swap">
<style>
  :root {
    --paper: #efe6d2;
    --ink: #3d2a1c;
    --fold: #b9ad97;
    --leaf: #8dc63f;
    --eco: rgba(150, 190, 80, 0.55);
    --splash-yellow: #d9df5a;
    --splash-orange: #f0a25a;
    --splash-teal: #5fc59e;
    --splash-blue: #6ccbef;
  }
  * { margin: 0; padding: 0; box-sizing: border-box; }
  html, body { width: 1200px; height: 849px; overflow: hidden; background: var(--paper); }
  .brochure {
    position: relative; width: 1200px; height: 849px; overflow: hidden;
    background: var(--paper); color: var(--ink);
    font-family: "PT Sans", sans-serif;
  }
  .fold { position: absolute; top: 0; width: 1px; height: 849px; background: var(--fold); z-index: 3; }
  .fold--one { left: 394px; }
  .fold--two { left: 794px; }

  .panel-heading {
    position: absolute; z-index: 2;
    font-family: "Dosis", sans-serif; font-weight: 700;
    font-size: 44px; line-height: 49px; letter-spacing: -0.3px;
  }
  .panel-copy { position: absolute; z-index: 2; font-size: 15px; line-height: 19px; }
  .panel-copy p + p { margin-top: 19px; }

  .vocs-heading { left: 42px; top: 106px; }
  .vocs-copy { left: 42px; top: 282px; width: 324px; }
  .owner-heading { left: 439px; top: 106px; }
  .owner-copy { left: 439px; top: 282px; width: 330px; }

  .eco-word {
    position: absolute; left: 62px; top: 515px; z-index: 1;
    font-family: "Quicksand", sans-serif; font-weight: 300;
    font-size: 265px; line-height: 265px; letter-spacing: 8px;
    color: var(--eco);
  }
  .splash-soft {
    position: absolute; left: 363px; top: 472px; width: 242px; height: 290px; z-index: 0;
    background: linear-gradient(160deg, rgba(217,223,90,0.25), rgba(217,223,90,0.5));
  }

  .brand {
    position: absolute; left: 859px; top: 52px; width: 290px;
    display: flex; align-items: center; gap: 10px;
    font-family: "Dosis", sans-serif; font-weight: 700;
    font-size: 30px; line-height: 34px; color: var(--ink); text-transform: uppercase;
  }
  .brand-square { width: 22px; height: 22px; background: var(--leaf); flex: none; }

  .splash-bright {
    position: absolute; left: 835px; top: 188px; width: 363px; height: 465px; z-index: 1;
    background: linear-gradient(160deg,
      rgba(240,162,90,0.45) 0%,
      rgba(95,197,158,0.45) 35%,
      rgba(108,203,239,0.45) 60%,
      rgba(217,223,90,0.5) 100%);
  }
  .specialities {
    position: absolute; left: 857px; top: 246px; z-index: 2;
    font-family: "Dosis", sans-serif; font-weight: 600; text-transform: uppercase; color: var(--ink);
  }
  .specialities span { display: block; }
  .specialities .lead { font-size: 35px; line-height: 40px; letter-spacing: 1.5px; }
  .specialities .major { font-size: 60px; line-height: 56px; letter-spacing: 3px; }
  .specialities .minor { font-size: 44px; line-height: 46px; letter-spacing: 1.5px; }
  .specialities .trail { font-size: 22px; line-height: 26px; letter-spacing: 1px; }

  .contact {
    position: absolute; left: 794px; top: 728px; width: 406px;
    text-align: center; font-weight: 700; font-size: 17px; line-height: 20px;
  }
</style>
</head>
<body>
<div class="brochure">
  <div class="fold fold--one"></div>
  <div class="fold fold--two"></div>

  <div class="splash-soft" role="img" aria-label="Yellow-green paint splash illustration"></div>
  <div class="eco-word" aria-hidden="true">ECO</div>

  <h2 class="panel-heading vocs-heading">VOCs=VOLATILE<br>ORGANIC<br>COMPOUNDS</h2>
  <div class="panel-copy vocs-copy">
    <p>VOCs are hazardous chemicals that are emitted from paints. This occurs even after the paint has dried; paints can continue too emit VOCs for several years after application. By using low VOC emitting paints, fewer chemicals are released than traditional paints. In choosing a zero VOC option, you will experience no odour after the paint has dried and will be helping improve air quality both inside and outside your home or business.</p>
    <p>At Fern Lodge Painting we choose to use these products and a green business approach because we care about our clients, workers and the overall environment.</p>
    <p>We can help make a difference, not just by changing the colour of your home or business but by giving you a better, safer environment in which to live and work.</p>
  </div>

  <h2 class="panel-heading owner-heading">ABOUT<br>THE<br>OWNER</h2>
  <div class="panel-copy owner-copy">
    <p>Gordon Lodge has been painting for over 20 years. He is an accredited Green Painter and is often called upon by architects and builders to provide advice on sustainable products and methods.</p>
  </div>

  <div class="brand">
    <span class="brand-square"></span>
    <span>Fern Lodge Painting</span>
  </div>

  <div class="splash-bright" role="img" aria-label="Colourful paint splash illustration in orange, green, blue and yellow"></div>

  <h1 class="specialities">
    <span class="lead">Specialising in:</span>
    <span class="major">Non Toxic</span>
    <span class="minor">Eco Friendly</span>
    <span class="trail">&amp; Heat Reflective Paints</span>
  </h1>

  <div class="contact">
    <div>www.fernlodge.biz</div>
    <div>phone 040 318 2694</div>
    <div>painting@fernlodge.biz</div>
  </div>
</div>
</body>
</html>
```